Easy Business Card / Presentation Cover Design Project

We are looking for a business card design, covers for powerpoint presentations for investors, and possibly simple stationary for a Chicago real estate development firm. Our new logo is attached below.

We rehab and provide newly constructed homes. We are not a real estate brokerage firm (i.e., agents such as Meridale 47) and only operate in the Chicago area.

In terms of design, sophisticated and high end that would appeal to investors (theme should resemble investment banks, hedge funds, private equity rather than tech startup).

Target Market(s)

Investors, banks, financing sources

Industry/Entity Type

Real Estate

Requirements
Must have
• Two deliverables here. 1) Business card 2) Covers for powerpoint presentation.

Must be able to look sophisticated and high end when printed. Please think through the type of printing that will be needed. Would prefer something that can be printed in raised ink but digital is ok as well.

Will be printed on heavy paper.

Business Card: Horizontal Layout, no black backgrounds,

For presentation front cover, should include logo only. For back cover, should include contact info. Horizontal and should not contain any information that will need to be changed (i.e. date or client name)
Nice to have
• Would like to have the edges colored but not required. Please show multiple designs
Should not have
• Should not have any die cut or embossed type of designs. Shape should be standard size.

We are not a design firm, a retail firm, or a consumer product firm.

Please do not incorporate a house, buildings, etc. This must be very professional looking.

```html
<!DOCTYPE html>
<html lang="en">
<head>
<meta charset="utf-8">
<title>Orrin Realty — Business Card</title>
<link href="https://fonts.googleapis.com/css2?family=Tinos:wght@400;700&family=Arimo:wght@400&display=swap" rel="stylesheet">
<style>
  :root {
    --backdrop: #ece9e4;
    --band-dark: #c9ccd1;
    --band-mid: #d6d9dd;
    --band-light: #e4e6e9;
    --rule: #8e9094;
    --brand-blue: #1a73d9;
    --ink: #2b2b2b;
    --ink-soft: #4a4a4a;
    --tint-blue: rgba(170, 210, 240, 0.35);
    --tint-grey: rgba(200, 204, 210, 0.25);
  }
  * { box-sizing: border-box; margin: 0; padding: 0; }
  html, body { width: 1200px; height: 1000px; overflow: hidden; }
  body { background: var(--backdrop); position: relative; }

  .card {
    position: absolute;
    width: 537px;
    height: 290px;
    top: 355px;
    overflow: hidden;
    box-shadow: 3px 4px 8px rgba(0,0,0,0.35);
  }
  .card--front { left: 60px; }
  .card--back { left: 607px; background: #fff; }

  /* Front */
  .front-bands {
    position: absolute; inset: 0;
    background: linear-gradient(to bottom,
      var(--band-dark) 0, var(--band-dark) 100px,
      var(--band-light) 100px, var(--band-light) 190px,
      var(--band-mid) 190px, var(--band-mid) 100%);
  }
  .front-tint {
    position: absolute; left: 150px; top: 0; width: 387px; height: 290px;
    background: linear-gradient(to right, rgba(170,210,240,0) 0, var(--tint-blue) 45%, var(--tint-grey) 100%);
  }
  .front-glow {
    position: absolute; inset: 0;
    background: linear-gradient(to right, rgba(255,255,255,0) 20%, rgba(255,255,255,0.6) 45%, rgba(255,255,255,0) 75%);
  }

  .brand {
    position: absolute;
    display: flex; align-items: center; gap: 10px;
  }
  .brand-dot {
    width: 30px; height: 30px; border-radius: 50%;
    background: var(--brand-blue);
  }
  .brand-name {
    font-family: "Tinos", serif; font-weight: 400;
    font-size: 26px; line-height: 30px; color: var(--ink); letter-spacing: 0.5px;
  }
  .card--front .brand { left: 200px; top: 125px; }
  .card--back .brand { left: 44px; top: 26px; }

  /* Back */
  .back-header {
    position: absolute; left: 0; top: 0; width: 100%; height: 88px;
    background: var(--band-dark);
  }
  .back-rule {
    position: absolute; left: 0; top: 88px; width: 100%; height: 5px;
    background: var(--rule);
  }
  .back-tint {
    position: absolute; left: 290px; top: 93px; width: 247px; height: 197px;
    background: linear-gradient(to right, rgba(170,210,240,0) 0, var(--tint-blue) 60%, var(--tint-grey) 100%);
  }
  .holder { position: absolute; left: 40px; top: 116px; }
  .holder-name {
    font-family: "Tinos", serif; font-weight: 700;
    font-size: 25px; color: var(--brand-blue); line-height: 1;
  }
  .holder-position {
    font-family: "Arimo", sans-serif; font-size: 18px;
    color: var(--ink-soft); letter-spacing: 0.5px; margin-top: 4px;
  }
  .contact {
    position: absolute; left: 40px; top: 186px;
    list-style: none;
    font-family: "Arimo", sans-serif; font-size: 16px;
    color: var(--ink); line-height: 22px;
  }
</style>
</head>
<body>
  <section class="card card--front" aria-label="Business card front">
    <div class="front-bands"></div>
    <div class="front-tint" role="img" aria-label="Soft pale blue decorative area"></div>
    <div class="front-glow"></div>
    <div class="brand">
      <span class="brand-dot"></span>
      <span class="brand-name">Orrin Realty</span>
    </div>
  </section>

  <section class="card card--back" aria-label="Business card back">
    <div class="back-header"></div>
    <div class="back-rule"></div>
    <div class="back-tint" role="img" aria-label="Soft pale blue decorative area"></div>
    <div class="brand">
      <span class="brand-dot"></span>
      <span class="brand-name">Orrin Realty</span>
    </div>
    <div class="holder">
      <p class="holder-name">YOUR NAME HERE</p>
      <p class="holder-position">YOUR POSITION HERE</p>
    </div>
    <ul class="contact">
      <li>Address:your address here</li>
      <li>E-mail:youremail@here.com</li>
      <li>Contact:your contact here</li>
      <li>Website:your website here</li>
    </ul>
  </section>
</body>
</html>
```